Electrical contracting business specialising in smoke detector installation needs flyer design

i need a flyer design made up highlighting the fact that the Qld legislation is changing on smoke detectors in homes for everyones safety. I am an electrical contractor ( Tandrell Electrical) specialising in smoke detector installation to comply with the new Qld legislation. Some of the wording that can be used-
When you sleep, your sense of smell also sleeps. If a fire starts, toxic fumes canovercome you. Photoelectric smoke alarms see smoke and will alert you early, so you can escape. With interconnected alarms, you will be alerted no matter where you are, or where the fire starts.
New legislation specifies the type, positioning and interconnectedness of alarms, which are critical factors for an early warning and a quick escape.
To give your family the best chance of surviving a house fire, update your smoke alarms to match the new legislation as soon as you can. Call ME on 0418362957

Target Market(s)

Body Corporates , people selling and renting their properties

Industry/Entity Type

Electrician

Colors

Designer to choose colors to be used in the design.

Requirements
Must have
• Safety aspect.

```html
<!DOCTYPE html>
<html lang="en">
<head>
<meta charset="utf-8">
<title>New Smoke Alarm Legislation – Tandrell Electrical</title>
<link href="https://fonts.googleapis.com/css2?family=Montserrat:wght@500;600;700&family=Source+Sans+3:wght@400;600&display=swap" rel="stylesheet">
<style>
  :root{
    --purple-deep:#1c0f3a;
    --purple-mid:#341763;
    --purple-glow:#4a1f80;
    --band-black:#050307;
    --gold:#e0a03a;
    --gold-text:#eba23a;
    --white:#ffffff;
    --footer-grey:#4a4a4c;
  }
  *{margin:0;padding:0;box-sizing:border-box}
  html,body{width:848px;height:1200px;overflow:hidden;background:var(--band-black)}
  .flyer{position:relative;width:848px;height:1200px;overflow:hidden;color:var(--white);
    font-family:"Source Sans 3",Arial,sans-serif}
  .band{position:absolute;left:0;width:848px}
  .band--existing{top:0;height:470px;
    background:radial-gradient(ellipse at 75% 10%,var(--purple-glow) 0%,transparent 55%),
               linear-gradient(135deg,var(--purple-deep) 0%,var(--purple-mid) 45%,var(--purple-deep) 100%)}
  .band--sale{top:470px;height:302px;
    background:linear-gradient(90deg,#1e0d33 0%,var(--band-black) 30%,var(--band-black) 100%)}
  .band--new{top:772px;height:384px;
    background:radial-gradient(ellipse at 20% 20%,var(--purple-glow) 0%,transparent 55%),
               linear-gradient(160deg,var(--purple-mid) 0%,var(--purple-deep) 60%,#120822 100%)}
  .band--foot{top:1156px;height:44px;background:var(--footer-grey)}

  .title-bar{position:absolute;left:0;top:37px;width:671px;height:68px;background:var(--gold);
    display:flex;align-items:center;padding-left:74px}
  .title-bar h1{font-family:"Montserrat",sans-serif;font-weight:700;font-size:31px;letter-spacing:.3px}

  .section-title{position:absolute;font-family:"Montserrat",sans-serif;font-weight:600;font-size:15.5px;
    text-decoration:underline;text-underline-offset:3px;text-decoration-thickness:1.5px;white-space:nowrap;letter-spacing:-.3px}
  .section-title--existing{left:314px;top:133px}
  .section-title--sale{left:130px;top:487px}
  .section-title--new{left:69px;top:781px;letter-spacing:2.55px;word-spacing:-1px}

  .date{position:absolute;font-family:"Montserrat",sans-serif;font-weight:700;font-size:15px;
    color:var(--gold-text);text-decoration:underline;text-underline-offset:2px;text-decoration-thickness:1.2px;white-space:nowrap}
  .subhead{position:absolute;font-family:"Montserrat",sans-serif;font-weight:700;font-size:15px;
    text-decoration:underline;text-underline-offset:2px;white-space:nowrap}

  .copy{position:absolute;font-size:12.2px;line-height:15.4px;white-space:nowrap}
  .rules{position:absolute;left:348px;font-size:10.2px;line-height:13.6px;white-space:nowrap}
  .rules p + p{margin-top:13.6px}

  .brand-mark{position:absolute;left:199px;top:1066px;width:76px;height:61px;background:#3a3434}
  .brand-name{position:absolute;left:297px;top:1081px;font-family:"Montserrat",sans-serif;font-weight:600;font-size:16px;white-space:nowrap}
  .brand-phone{position:absolute;left:297px;top:1101px;font-family:"Montserrat",sans-serif;font-weight:700;font-size:16px;color:var(--gold-text)}
  .partner{position:absolute;top:1047px}
</style>
</head>
<body>
<main class="flyer">
  <div class="band band--existing"></div>
  <div class="band band--sale"></div>
  <div class="band band--new"></div>
  <div class="band band--foot"></div>

  <header class="title-bar"><h1>NEW SMOKE ALARM LEGISLATION</h1></header>

  <!-- Existing dwellings -->
  <h2 class="section-title section-title--existing">FOR EXISTING DWELLINGS</h2>
  <h3 class="date" style="left:74px;top:163px">From 1 January 2017</h3>
  <p class="copy" style="left:74px;top:181px">When replacing smoke alarms, they must be<br>of a photoelectric type which complies with<br>Australian Standard (AS) 3786-2014.</p>
  <h3 class="subhead" style="left:74px;top:245px">Replacing smoke alarms</h3>
  <p class="copy" style="left:74px;top:263px">Existing smoke alarms manufactured more<br>than ten years ago must be replaced. (Note:<br>Smoke alarms should have the date of<br>manufacture stamped on them.)<br>Smoke alarms that do not operate when<br>tested must be replaced immediately.<br>Existing hardwired smoke alarms that<br>need replacement must be replaced with a<br>hardwired smoke alarm.</p>

  <h3 class="date" style="left:348px;top:163px">From 1 January 2027</h3>
  <div class="rules" style="top:180px">
    <p>Smoke alarms in all dwellings must:<br>i) be photoelectric (AS 3786-2014); and<br>ii) not also contain an ionisation sensor; and<br>iii) be less than 10 years old; and<br>iv) operate when tested; and<br>v) be interconnected with every other smoke alarm in the dwelling so all activate<br>together.</p>
    <p>Smoke alarms must be installed on each storey:</p>
    <p>i) in each bedroom; and<br>ii) in hallways which connect bedrooms and the rest of the<br>dwelling; or<br>iii) if there is no hallway, between the bedrooms and other parts<br>of the storey; and<br>iv) if there are no bedrooms on a storey at least one smoke alarm must be installed in<br>the most likely path of travel to exit the dwelling.</p>
    <p>Smoke alarms must be either hardwired or powered by a nonremovable<br>10-year battery.</p>
  </div>

  <!-- Sold / leased -->
  <h2 class="section-title section-title--sale">DWELLINGS BEING SOLD, LEASED OR AN EXISTING LEASE IS RENEWED</h2>
  <h3 class="date" style="left:74px;top:517px">From 1 January 2017</h3>
  <p class="copy" style="left:74px;top:534px">Requirements as for<br>existing dwellings.<br>Existing landlord’s and<br>tenant’s obligations<br>regarding the installation<br>and testing of smoke<br>alarms continue.<br>Property sellers must<br>continue to lodge a Form<br>24 with the Queensland<br>Land Registry Office<br>stating the requirements<br>of the smoke alarm<br>legislation have been</p>

  <h3 class="date" style="left:348px;top:517px">From 1 January 2022</h3>
  <div class="rules" style="top:534px">
    <p>Smoke alarms in the dwelling must:<br>i) be photoelectric (AS 3786-2014); and<br>ii) not also contain an ionisation sensor; and<br>iii) be less than 10 years old; and<br>iv) operate when tested; and<br>v) be interconnected with every other smoke alarm in the dwelling so all activate<br>together.</p>
    <p>Smoke alarms must be installed on each storey:<br>i) in each bedroom; and<br>ii) in hallways which connect bedrooms and the rest of the dwelling; or<br>iii) if there is no hallway, between the bedrooms and other parts of the storey; and<br>iv) if there are no bedrooms on a storey at least one smoke alarm must be installed in<br>the most likely path of travel to exit the dwelling.</p>
    <p>Smoke alarms must be hardwired or powered by a non-removable 10-year battery.</p>
  </div>

  <!-- New / renovated -->
  <h2 class="section-title section-title--new">NEW DWELLINGS AND DWELLINGS BEING SUBSTANTIALLY RENOVATED</h2>
  <h3 class="date" style="left:74px;top:812px">From 1 January 2017</h3>
  <p class="copy" style="left:74px;top:829px">The development<br>approval process for new<br>dwellings and substantial<br>renovations will ensure<br>that building approvals<br>received on or after this<br>date will bring dwellings<br>into compliance with the<br>new laws.<br>met.</p>

  <div class="rules" style="top:812px">
    <p>Smoke alarms in the dwelling must:<br>i) be photoelectric (AS 3786-2014); and<br>ii) not also contain an ionisation sensor; and<br>iii) be hardwired to the mains power supply with a secondary power source (i.e. battery);<br>and<br>iv) be interconnected with every other smoke alarm in the dwelling so all activate together.</p>
    <p>Smoke alarms must be installed on each storey:</p>
    <p>i) in each bedroom; and<br>ii) in hallways which connect bedrooms and the rest of the dwelling; or<br>iii) if there is no hallway, between the bedrooms and other parts of the storey; and<br>iv) if there are no bedrooms on a storey at least one smoke alarm must be installed in<br>the most likely path of travel to exit the dwelling.</p>
  </div>

  <!-- Contact -->
  <div class="brand-mark" aria-hidden="true"></div>
  <p class="brand-name">Tandrell Electrical</p>
  <p class="brand-phone">0418362957</p>
  <svg class="partner" style="left:484px" width="68" height="82" viewBox="0 0 68 82" role="img" aria-label="Fire service partner badge">
    <circle cx="34" cy="44" r="32" fill="#8a2a2a"/>
  </svg>
  <svg class="partner" style="left:572px" width="66" height="82" viewBox="0 0 66 82" role="img" aria-label="State government partner badge">
    <rect x="5" y="8" width="56" height="66" fill="#ffffff"/>
  </svg>
</main>
</body>
</html>
```